Need business card designed for a Mobile RV Repair business

I need a business card designed

Welding sparks

Industry/Entity Type

Rv Repair , Mobile Welding & Fabrication

Contact Information for Business Card

Colors
0054AA
0677BA
7BADD7
CADEEF
E8F1F8

Requirements
Nice to have
• welding sparks, list of services, welding vector

```html
<!DOCTYPE html>
<html lang="en">
<head>
<meta charset="UTF-8">
<title>Ridgeline Mobile – Business Card</title>
<link href="https://fonts.googleapis.com/css2?family=Lato:wght@400;700;900&display=swap" rel="stylesheet">
<style>
  :root {
    --blue-deep: #0054AA;
    --blue-mid: #0677BA;
    --blue-soft: #7BADD7;
    --blue-pale: #CADEEF;
    --blue-mist: #E8F1F8;
    --paper: #ffffff;
    --ink: #1c1c1c;
    --stage: #2e3033;
    --ghost: #eef0f2;
  }
  * { box-sizing: border-box; margin: 0; padding: 0; }
  html, body { width: 1200px; height: 1122px; overflow: hidden; }
  body {
    background: var(--stage);
    font-family: "Lato", sans-serif;
    position: relative;
  }
  .card {
    position: absolute;
    left: 160px;
    width: 880px;
    height: 503px;
    background: var(--paper);
    border-radius: 28px;
    overflow: hidden;
  }
  .card--front { top: 40px; }
  .card--back { top: 579px; }

  /* Front: project gallery */
  .gallery {
    position: absolute;
    left: 18px; right: 18px; top: 18px;
    height: 318px;
    display: grid;
    grid-template-columns: 1fr 1fr 1fr 1fr;
    grid-template-rows: 1fr 1fr;
    gap: 8px;
  }
  .gallery__tile { border-radius: 2px; }
  .tile-frame    { background: linear-gradient(160deg, #c9ccd0, #8a8d91 70%, #5d6064); }
  .tile-room     { background: linear-gradient(170deg, #f1f1f1, #b9b9b9 55%, #3e3a38); }
  .tile-interior { background: linear-gradient(160deg, #cfcfcf, #6f6f6f 60%, #2a2a2a); }
  .tile-race     { background: linear-gradient(150deg, #c7d3de, #d8303a 45%, #3c4450); }
  .tile-gate     { background: linear-gradient(160deg, #b8b5ad, #8a7a62 55%, #3a3632); }
  .tile-trailer  { background: linear-gradient(160deg, #4d4a45, #d9d6d0 50%, #6a665f); }
  .tile-truck    { background: linear-gradient(170deg, #b9c6d2, #a38f6e 55%, #55575a); }
  .tile-hauler   { background: linear-gradient(170deg, #3f7fc8, #e9ecef 50%, #5a5c5f); }

  .services {
    position: absolute;
    left: 0; right: 0; bottom: 0;
    height: 150px;
    background: var(--blue-deep);
    color: var(--paper);
    display: flex;
    flex-direction: column;
    justify-content: center;
    align-items: center;
    text-align: center;
    text-transform: uppercase;
    font-weight: 700;
    font-size: 19px;
    line-height: 1.35;
    letter-spacing: 0.3px;
  }
  .services__sep { margin: 0 4px; }

  /* Back: identity side */
  .welder-art {
    position: absolute;
    left: 60px; top: 150px;
    width: 380px; height: 340px;
    background: var(--ghost);
    border-radius: 120px 140px 40px 60px;
  }
  .brand {
    position: absolute;
    right: 60px; top: 70px;
    display: flex;
    align-items: center;
    gap: 12px;
    color: var(--blue-deep);
    font-weight: 900;
    font-size: 42px;
    letter-spacing: 0.5px;
  }
  .brand__dot {
    width: 22px; height: 22px;
    border-radius: 50%;
    background: var(--blue-deep);
  }
  .person {
    position: absolute;
    left: 80px; top: 240px;
  }
  .person__name {
    color: var(--blue-deep);
    font-weight: 900;
    font-size: 46px;
    letter-spacing: 1px;
    text-transform: uppercase;
    line-height: 1;
  }
  .person__role {
    color: var(--ink);
    font-size: 26px;
    margin-top: 8px;
  }
  .rule {
    position: absolute;
    left: 80px; right: 60px; top: 345px;
    height: 3px;
    background: var(--blue-deep);
  }
  .contact {
    position: absolute;
    left: 80px; top: 372px;
    list-style: none;
    color: var(--ink);
    font-size: 27px;
  }
  .contact__item {
    display: flex;
    align-items: center;
    gap: 14px;
    margin-bottom: 12px;
  }
  .contact__icon { width: 24px; height: 24px; flex: none; }
</style>
</head>
<body>

<section class="card card--front" aria-label="Business card front">
  <div class="gallery">
    <div class="gallery__tile tile-frame" role="img" aria-label="Photo of a steel trailer frame under fabrication"></div>
    <div class="gallery__tile tile-room" role="img" aria-label="Photo of a finished trailer interior room"></div>
    <div class="gallery__tile tile-interior" role="img" aria-label="Photo of a custom mobile office interior"></div>
    <div class="gallery__tile tile-race" role="img" aria-label="Photo of a red race car hauler with tube frame"></div>
    <div class="gallery__tile tile-gate" role="img" aria-label="Photo of a welded decorative steel gate"></div>
    <div class="gallery__tile tile-trailer" role="img" aria-label="Photo of an enclosed cargo trailer in a workshop"></div>
    <div class="gallery__tile tile-truck" role="img" aria-label="Photo of a semi truck with trailer under construction"></div>
    <div class="gallery__tile tile-hauler" role="img" aria-label="Photo of a white fifth-wheel trailer outdoors"></div>
  </div>
  <div class="services">
    <p>Mobile Welding<span class="services__sep">✶</span>Aluminum, Steel &amp; Stainless<span class="services__sep">✶</span>Custom Welding &amp; Fabrication</p>
    <p>Fence &amp; Gate Customization<span class="services__sep">✶</span>General Welding Repair<span class="services__sep">✶</span>Production Welding</p>
    <p>RV &amp; Motorhome Repair<span class="services__sep">✶</span>Electrical Systems<span class="services__sep">✶</span>Plumbing<span class="services__sep">✶</span>Trailer Frame &amp; Repair</p>
    <p>Construction Welding Repair</p>
  </div>
</section>

<section class="card card--back" aria-label="Business card back">
  <div class="welder-art" role="img" aria-label="Faint illustration of a welder in a welding helmet"></div>
  <div class="brand"><span class="brand__dot"></span>RIDGELINE MOBILE</div>
  <div class="person">
    <h1 class="person__name">Marco Delgado</h1>
    <p class="person__role">Owner</p>
  </div>
  <div class="rule"></div>
  <ul class="contact">
    <li class="contact__item">
      <svg class="contact__icon" viewBox="0 0 24 24" aria-hidden="true">
        <path fill="#0054AA" d="M6.6 10.8a15.2 15.2 0 0 0 6.6 6.6l2.2-2.2a1 1 0 0 1 1-.25 11.4 11.4 0 0 0 3.6.57 1 1 0 0 1 1 1V20a1 1 0 0 1-1 1A17 17 0 0 1 3 4a1 1 0 0 1 1-1h3.5a1 1 0 0 1 1 1c0 1.25.2 2.45.57 3.57a1 1 0 0 1-.25 1z"/>
      </svg>
      <span>555.013.2748</span>
    </li>
    <li class="contact__item">
      <svg class="contact__icon" viewBox="0 0 24 24" aria-hidden="true">
        <rect x="2" y="5" width="20" height="14" rx="1.5" fill="#0054AA"/>
        <path d="M3 6.5l9 6.5 9-6.5" fill="none" stroke="#fff" stroke-width="1.6"/>
      </svg>
      <span>ridgelinemobile@mailbox.com</span>
    </li>
  </ul>
</section>

</body>
</html>
```